Criação de Papelaria Profissional para Consultoria de Negócios
" Somos uma empresa de consultoria para transportadoras, atuamos de forma operacional, fazemos um diagnóstico dos problemas da empresa, desenhamos processos, treinamos e auditamos o andamento, atuamos em todas os departamentos de uma transportadora. "

```html
<!DOCTYPE html>
<html lang="pt-BR">
<head>
<meta charset="UTF-8">
<title>Trilha Consultoria – Papelaria</title>
<link rel="stylesheet" href="https://fonts.googleapis.com/css2?family=Roboto:wght@400;500;700;900&display=swap">
<style>
  :root {
    --stage: #2b2b2d;
    --paper: #ffffff;
    --paper-shade: #eceef1;
    --orange: #f47a20;
    --orange-light: #ffa040;
    --blue: #2e5f9e;
    --blue-dark: #1d4478;
    --ink: #2e5f9e;
    --footer-text: #dfe8f4;
    --grey-band: #e6e7ea;
  }
  * { box-sizing: border-box; margin: 0; padding: 0; }
  html, body {
    width: 1200px; height: 1200px; overflow: hidden;
    background: var(--stage);
    font-family: "Roboto", Arial, sans-serif;
  }
  .canvas { position: relative; width: 1200px; height: 1200px; }

  .envelope-back, .folder-front {
    position: absolute; top: 223px; height: 766px;
    background: var(--paper);
    box-shadow: 0 10px 30px rgba(0,0,0,.45);
    overflow: hidden;
  }
  .envelope-back { left: 53px; width: 530px; }
  .folder-front { left: 634px; width: 514px; }

  .envelope-flap {
    position: absolute; left: 0; top: 0; width: 100%; height: 100px;
  }

  .envelope-watermark {
    position: absolute; left: 0; top: 185px; width: 463px; height: 456px;
    background: linear-gradient(90deg, var(--paper-shade) 0%, #f5f6f8 60%, rgba(255,255,255,0) 100%);
    border-radius: 0 60px 60px 0;
  }

  .folder-corner-art {
    position: absolute; left: 0; top: 485px; width: 218px; height: 240px;
    background: linear-gradient(135deg, var(--orange) 0%, var(--orange-light) 45%, var(--blue) 100%);
    border-radius: 0 40px 40px 0;
  }

  .brand { position: absolute; line-height: 1; }
  .brand-row { display: flex; align-items: center; gap: 8px; }
  .brand-mark { border-radius: 50%; background: var(--orange); flex: none; }
  .brand-name { font-weight: 900; color: var(--ink); letter-spacing: -0.5px; }
  .brand-tagline {
    display: block; color: var(--orange); font-weight: 400;
    text-transform: uppercase;
  }

  .envelope-back .brand { left: 180px; top: 656px; }
  .envelope-back .brand-name { font-size: 40px; }
  .envelope-back .brand-mark { width: 24px; height: 24px; }
  .envelope-back .brand-tagline { font-size: 11px; margin-left: 34px; margin-top: 1px; letter-spacing: 1.5px; }

  .folder-front .brand { left: 117px; top: 318px; }
  .folder-front .brand-name { font-size: 66px; }
  .folder-front .brand-mark { width: 38px; height: 38px; }
  .folder-front .brand-tagline { font-size: 17px; margin-left: 48px; margin-top: 2px; letter-spacing: 2.5px; }

  .envelope-footer {
    position: absolute; left: 0; bottom: 0; width: 100%; height: 34px;
    background: var(--blue);
    display: flex; align-items: center; justify-content: space-around;
    padding: 0 10px;
  }
  .contact-item {
    display: flex; align-items: center; gap: 5px;
    color: var(--footer-text); font-size: 7px; white-space: nowrap;
  }
  .contact-icon { width: 11px; height: 11px; flex: none; }

  .folder-stripe { position: absolute; left: 0; width: 100%; }
  .folder-stripe.blue { top: 725px; height: 12px; background: var(--blue); }
  .folder-stripe.grey { top: 737px; height: 29px; background: var(--grey-band); }
</style>
</head>
<body>
<main class="canvas">

  <section class="envelope-back" aria-label="Envelope – verso">
    <svg class="envelope-flap" viewBox="0 0 530 100" preserveAspectRatio="none" aria-hidden="true">
      <defs>
        <linearGradient id="flapFill" x1="0" y1="0" x2="0" y2="1">
          <stop offset="0" stop-color="#ffa040"/>
          <stop offset="1" stop-color="#f47a20"/>
        </linearGradient>
      </defs>
      <path d="M0 0 H530 V48 Q530 96 482 96 H48 Q0 96 0 48 Z" fill="url(#flapFill)"/>
    </svg>

    <div class="envelope-watermark" role="img" aria-label="Grafismo institucional suave em cinza claro"></div>

    <div class="brand">
      <div class="brand-row">
        <span class="brand-mark"></span>
        <span class="brand-name">Trilha</span>
      </div>
      <span class="brand-tagline">Consultoria</span>
    </div>

    <footer class="envelope-footer">
      <span class="contact-item">
        <svg class="contact-icon" viewBox="0 0 12 12"><path d="M6 1a3.5 3.5 0 0 0-3.5 3.5C2.5 7.5 6 11 6 11s3.5-3.5 3.5-6.5A3.5 3.5 0 0 0 6 1z" fill="#dfe8f4"/><circle cx="6" cy="4.5" r="1.2" fill="#2e5f9e"/></svg>
        Rua das Flores, 210 – Centro – Curitiba
      </span>
      <span class="contact-item">
        <svg class="contact-icon" viewBox="0 0 12 12"><path d="M3 1.5l2 2-1 1.2a6 6 0 0 0 3.3 3.3l1.2-1 2 2-1.3 1.5C5.5 10.5 1.5 6.5 1.5 2.8z" fill="#dfe8f4"/></svg>
        (41) 3000-0000
      </span>
      <span class="contact-item">
        <svg class="contact-icon" viewBox="0 0 12 12"><path d="M6 1a3.5 3.5 0 0 0-3.5 3.5C2.5 7.5 6 11 6 11s3.5-3.5 3.5-6.5A3.5 3.5 0 0 0 6 1z" fill="#dfe8f4"/><circle cx="6" cy="4.5" r="1.2" fill="#2e5f9e"/></svg>
        Av. Brasil, 1500, sala 4 – Curitiba
      </span>
      <span class="contact-item">
        <svg class="contact-icon" viewBox="0 0 12 12"><circle cx="6" cy="6" r="4.5" fill="none" stroke="#dfe8f4" stroke-width="1.2"/><path d="M1.5 6h9M6 1.5c2 2.5 2 6.5 0 9M6 1.5c-2 2.5-2 6.5 0 9" fill="none" stroke="#dfe8f4" stroke-width=".9"/></svg>
        trilhaconsultoria.com.br
      </span>
    </footer>
  </section>

  <section class="folder-front" aria-label="Pasta – capa">
    <div class="brand">
      <div class="brand-row">
        <span class="brand-mark"></span>
        <span class="brand-name">Trilha</span>
      </div>
      <span class="brand-tagline">Consultoria</span>
    </div>

    <div class="folder-corner-art" role="img" aria-label="Grafismo institucional em laranja e azul"></div>

    <div class="folder-stripe blue"></div>
    <div class="folder-stripe grey"></div>
  </section>

</main>
</body>
</html>
```